New design for Kindle Ledger Website - landing page plus 3 carousel pages

We have a new website we want to launch for 501c3 organizations - Faith-based organizations, not for profit organizations, colleges and universities. Note - this is a design only project. We want to see designs for the landing page and the 3 other pages - Faith-based organizations, not for profit organizations, colleges and universities.
Format: We expect to create this website in Wix so requirement is to make the graphics Wix compatible
See Dossier attached for more details, 4 wireframes (1 landing page and 3 carousel pages), and brand guidelines
Please be creative and and make the visuals engaging. We do NOT want you to simply replicate what is in the wireframe. We are looking for a totally new, fresh and engaging design.

```html
<!DOCTYPE html>
<html lang="en">
<head>
<meta charset="utf-8">
<title>Kindle Ledger Technologies – 501c3 Organizations</title>
<link rel="stylesheet" href="https://fonts.googleapis.com/css2?family=Montserrat:wght@500;600;700;800&family=Poppins:wght@400;500;600&display=swap">
<style>
  :root{
    --navy:#0b1a3b;
    --navy-deep:#081530;
    --green:#1ccb8c;
    --green-dark:#12a873;
    --white:#ffffff;
    --muted:#c9d2e3;
    --line:#2a3a60;
    --head:"Montserrat", Arial, sans-serif;
    --body:"Poppins", Arial, sans-serif;
  }
  *{box-sizing:border-box;margin:0;padding:0}
  html,body{width:1200px;height:4320px;overflow:hidden}
  body{background:var(--navy);color:var(--white);font-family:var(--body);position:relative}
  .abs{position:absolute}
  .center{left:0;width:1200px;text-align:center}
  .glow{position:absolute;pointer-events:none}
  .glow--top{left:0;top:400px;width:1200px;height:330px;background:radial-gradient(ellipse 60% 45% at 50% 55%,rgba(48,92,160,.45),rgba(11,26,59,0) 70%)}
  .glow--process{left:0;top:1380px;width:1200px;height:370px;background:radial-gradient(ellipse 70% 50% at 50% 65%,rgba(48,92,160,.5),rgba(11,26,59,0) 72%)}
  .glow--news{left:0;top:3720px;width:1200px;height:320px;background:radial-gradient(ellipse 55% 45% at 50% 50%,rgba(48,92,160,.35),rgba(11,26,59,0) 72%)}

  .brand{display:flex;align-items:center;gap:12px}
  .brand__dot{width:52px;height:52px;border:5px solid var(--green);border-radius:50%}
  .brand__name{font-family:var(--head);font-weight:600;font-size:25px;line-height:1.05;color:var(--white)}
  .nav{display:flex;gap:31px;font-family:var(--head);font-weight:600;font-size:13px;letter-spacing:.2px}
  .login{left:992px;top:42px;width:123px;height:52px;border:2px solid var(--white);border-radius:26px;display:flex;align-items:center;justify-content:center;font-family:var(--head);font-weight:600;font-size:13px}

  .h1{font-family:var(--head);font-weight:800;font-size:54px;letter-spacing:.5px}
  .h2{font-family:var(--head);font-weight:800;font-size:44px}
  .lede{font-size:14.5px;line-height:23px;color:var(--muted)}

  .org{width:240px;text-align:center}
  .org__label{margin-top:10px;font-family:var(--head);font-weight:700;font-size:19px;line-height:28px;color:var(--green)}

  .role{font-family:var(--head);font-weight:600;font-size:26px;line-height:40px;text-align:center}

  .step{width:250px;text-align:center}
  .step__title{font-family:var(--head);font-weight:700;font-size:28px;margin-top:4px}
  .step__text{font-size:12.5px;line-height:21px;color:var(--muted);margin-top:6px}
  .step__num{font-family:var(--head);font-weight:800;font-size:32px;fill:var(--navy)}

  .btn{display:flex;align-items:center;justify-content:center;border-radius:40px;font-family:var(--head);font-weight:600;font-size:14px}
  .btn--solid{background:var(--green);color:var(--white)}
  .btn--ghost{border:2px solid var(--green);color:var(--green)}

  .give{font-family:var(--head);font-weight:700;font-size:28px;color:var(--green)}
  .amount{position:absolute;height:43px;border:2px solid var(--green);border-radius:22px;color:var(--green);font-family:var(--head);font-weight:600;font-size:21px;display:flex;align-items:center;justify-content:center}
  .amount--other{font-size:14px}
  .pay{position:absolute;top:2192px;height:26px;font-family:var(--head);font-weight:700;font-size:14px;color:var(--white);display:flex;align-items:center}

  .option{width:300px;text-align:center}
  .option__title{font-family:var(--head);font-weight:600;font-size:21px;line-height:30px;margin-top:34px}
  .option__brand{display:flex;align-items:center;justify-content:center;gap:7px;margin-top:14px;font-family:var(--head);font-weight:600;font-size:12px}
  .option__brand span.ring{width:22px;height:22px;border:3px solid var(--white);border-radius:50%}

  .video{left:85px;top:2430px;width:1030px;height:590px;border-radius:40px;overflow:hidden;background:linear-gradient(165deg,#6f7884 0%,#434b56 35%,#2b323b 65%,#1b2129 100%)}

  .perk{width:300px;text-align:center}
  .perk__title{font-family:var(--head);font-weight:700;font-size:29px;margin-top:14px}
  .perk__text{font-size:12.5px;line-height:21px;color:var(--muted);margin-top:8px}
  .divider{position:absolute;top:3260px;height:170px;border-left:1px dashed var(--line)}

  .subscribe{left:261px;top:3778px;width:676px;height:60px;display:flex}
  .subscribe__field{flex:1;background:var(--white);border-radius:30px 0 0 30px;color:#9aa3b4;font-size:13px;display:flex;align-items:center;padding-left:34px}
  .subscribe__send{width:141px;background:var(--green);border-radius:0 30px 30px 0;display:flex;align-items:center;justify-content:center;font-family:var(--head);font-weight:700;font-size:14px}
  .consent{left:305px;top:3851px;display:flex;align-items:center;gap:12px;font-size:15px;font-weight:500}
  .consent__box{width:20px;height:20px;border:2px solid var(--white);border-radius:3px}
  .fine{font-size:12px;line-height:17px;color:var(--muted)}

  .rule{position:absolute;left:85px;width:1030px;border-top:1px solid var(--line)}
  .footnav{display:flex;justify-content:center;gap:32px;font-family:var(--head);font-weight:600;font-size:13px}
</style>
</head>
<body>

<div class="glow glow--top"></div>
<div class="glow glow--process"></div>
<div class="glow glow--news"></div>

<header>
  <div class="abs brand" style="left:85px;top:34px">
    <span class="brand__dot"></span>
    <span class="brand__name">Kindle Ledger<br>Technologies</span>
  </div>
  <nav class="abs nav" style="left:441px;top:59px">
    <span>ABOUT US ⌄</span><span>NEWSROOM</span><span>PATENTS</span><span>CLIENTS</span><span>FAQ</span><span>CONTACT</span>
  </nav>
  <a class="abs login">LOG IN</a>
</header>

<h1 class="abs center h1" style="top:164px">501c3 ORGANIZATIONS</h1>
<p class="abs lede" style="left:180px;width:840px;top:241px;text-align:center">Lorem ipsum dolor sit amet, consectetur adipiscing elit. Maecenas quam risus, semper non nunc nec, egestas tincidunt quam. Duis eu nibh sit amet nisl imperdiet ornare at a neque.</p>

<svg width="0" height="0" style="position:absolute">
  <defs>
    <g id="org-hex">
      <polygon points="67,6 124,39 124,105 67,138 10,105 10,39" fill="none" stroke="#fff" stroke-width="6"/>
      <polygon points="67,22 110,47 110,97 67,122 24,97 24,47" fill="#1ccb8c"/>
      <circle cx="67" cy="6" r="7" fill="#fff"/><circle cx="124" cy="39" r="7" fill="#fff"/><circle cx="124" cy="105" r="7" fill="#fff"/>
      <circle cx="67" cy="138" r="7" fill="#fff"/><circle cx="10" cy="105" r="7" fill="#fff"/><circle cx="10" cy="39" r="7" fill="#fff"/>
    </g>
  </defs>
</svg>

<div class="abs org" style="left:247px;top:332px">
  <svg width="134" height="144" role="img" aria-label="Non profit organisation emblem"><use href="#org-hex"/></svg>
  <div class="org__label">NON PROFIT<br>ORGANISATION</div>
</div>
<div class="abs org" style="left:480px;top:334px">
  <svg width="134" height="144" role="img" aria-label="Faith-based organizations emblem"><use href="#org-hex"/></svg>
  <div class="org__label">FAITH-BASED<br>ORGANIZATIONS</div>
</div>
<div class="abs org" style="left:711px;top:334px">
  <svg width="134" height="144" role="img" aria-label="Colleges and universities emblem"><use href="#org-hex"/></svg>
  <div class="org__label">COLLEGES<br>AND UNIVERSITIES</div>
</div>

<div class="abs role center" style="top:675px;font-size:27px">501c3<br>ORGANIZATIONS</div>
<svg class="abs" style="left:410px;top:765px" width="380" height="330">
  <polygon points="188,8 372,321 4,321" fill="#fff"/>
  <g stroke="#0b1a3b" stroke-width="4" fill="none" stroke-linecap="round" stroke-linejoin="round">
    <path d="M188 102 V64 M176 78 L188 64 L200 78"/>
    <path d="M95 293 L125 270 M95 293 L99 277 M95 293 L112 292"/>
    <path d="M317 293 L287 270 M317 293 L313 277 M317 293 L300 292"/>
  </g>
  <circle cx="188" cy="212" r="50" fill="none" stroke="#0b1a3b" stroke-width="9"/>
  <text x="188" y="287" text-anchor="middle" font-family="Montserrat, Arial, sans-serif" font-weight="600" font-size="15" fill="#0b1a3b">Kindle Ledger</text>
</svg>
<div class="abs role" style="left:160px;width:300px;top:1073px">DATA OBJECT<br>"DONOR"</div>
<div class="abs role" style="left:758px;width:300px;top:1073px">DATA EXCHANGE<br>"BUYER"</div>

<h2 class="abs center h2" style="top:1250px;font-size:42px">PROCESS</h2>
<svg class="abs" style="left:0;top:1332px" width="1200" height="112">
  <g stroke="#c9d2e3" stroke-width="1.5" stroke-dasharray="7 6" fill="none">
    <line x1="258" y1="56" x2="412" y2="56"/><line x1="522" y1="56" x2="676" y2="56"/><line x1="786" y1="56" x2="940" y2="56"/>
  </g>
  <g stroke="#c9d2e3" stroke-width="1.5" fill="none">
    <path d="M330 50 L337 56 L330 62"/><path d="M594 50 L601 56 L594 62"/><path d="M858 50 L865 56 L858 62"/>
  </g>
  <g fill="#fff" stroke="#1ccb8c" stroke-width="5">
    <polygon points="204,4 249,30 249,82 204,108 159,82 159,30"/>
    <polygon points="468,4 513,30 513,82 468,108 423,82 423,30"/>
    <polygon points="731,4 776,30 776,82 731,108 686,82 686,30"/>
    <polygon points="994,4 1039,30 1039,82 994,108 949,82 949,30"/>
  </g>
  <g text-anchor="middle">
    <text class="step__num" x="204" y="67">01</text><text class="step__num" x="468" y="67">02</text>
    <text class="step__num" x="731" y="67">03</text><text class="step__num" x="994" y="67">04</text>
  </g>
</svg>
<div class="abs step" style="left:79px;top:1460px"><div class="step__title">Step 1</div><p class="step__text">Lorem ipsum dolor sit amet, consectetur adipiscing elit. Maecenas quam risus, semper</p></div>
<div class="abs step" style="left:343px;top:1460px"><div class="step__title">Step 2</div><p class="step__text">Lorem ipsum dolor sit amet, consectetur adipiscing elit. Maecenas quam risus, semper</p></div>
<div class="abs step" style="left:606px;top:1458px"><div class="step__title">Step 3</div><p class="step__text">Lorem ipsum dolor sit amet, consectetur adipiscing elit. Maecenas quam risus, semper</p></div>
<div class="abs step" style="left:869px;top:1460px"><div class="step__title">Step 4</div><p class="step__text">Lorem ipsum dolor sit amet, consectetur adipiscing elit. Maecenas quam risus, semper</p></div>
<a class="abs btn btn--solid" style="left:501px;top:1619px;width:193px;height:57px">DONATE DATA</a>

<h2 class="abs center h2" style="top:1858px">MY DONATION</h2>
<p class="abs center" style="top:1917px;font-size:15px;font-weight:500">All donations are tax deductible</p>

<div class="abs give" style="left:85px;top:1980px">I want to give</div>
<span class="amount" style="left:85px;top:2037px;width:111px">$25</span>
<span class="amount" style="left:225px;top:2037px;width:112px">$50</span>
<span class="amount" style="left:365px;top:2037px;width:111px">$100</span>
<span class="amount" style="left:85px;top:2103px;width:111px">$125</span>
<span class="amount" style="left:225px;top:2103px;width:112px">$150</span>
<span class="amount amount--other" style="left:365px;top:2103px;width:151px">Other Amount</span>

<span class="pay" style="left:87px">Veltra</span>
<span class="pay" style="left:161px">Orbix</span>
<span class="pay" style="left:240px">Findpay</span>
<span class="pay" style="left:318px">Amberline</span>
<span class="pay" style="left:404px">Paywell</span>
<a class="abs btn btn--solid" style="left:85px;top:2253px;width:264px;height:55px">DONATE WITH CREDIT CARD</a>

<div class="abs option" style="left:554px;top:1984px">
  <svg width="100" height="110" role="img" aria-label="Crypto donation icon"><polygon points="50,2 97,29 97,81 50,108 3,81 3,29" fill="#1ccb8c"/><circle cx="50" cy="55" r="22" fill="none" stroke="#fff" stroke-width="4"/></svg>
  <div class="option__title" style="margin-top:10px">Donate with Crypto<br>Powered by KLT</div>
  <div class="option__brand"><span class="ring"></span>Kindle Ledger Technologies</div>
  <a class="btn btn--ghost" style="width:122px;height:49px;margin:14px auto 0;font-size:13px">DONATE</a>
</div>
<div class="abs option" style="left:822px;top:1984px">
  <svg width="100" height="110" role="img" aria-label="Data donation icon"><polygon points="50,2 97,29 97,81 50,108 3,81 3,29" fill="#1ccb8c"/><ellipse cx="50" cy="48" rx="22" ry="8" fill="none" stroke="#fff" stroke-width="4"/><path d="M28 48 V70 Q50 80 72 70 V48" fill="none" stroke="#fff" stroke-width="4"/></svg>
  <div class="option__title" style="margin-top:10px">Donate with Data</div>
  <div class="option__brand" style="margin-top:44px"><span class="ring"></span>Kindle Ledger Technologies</div>
  <a class="btn btn--ghost" style="width:122px;height:49px;margin:14px auto 0;font-size:13px">DONATE</a>
</div>

<div class="abs video" role="img" aria-label="Video still: a hand pressing a donate key on a keyboard">
  <svg class="abs" style="left:423px;top:202px" width="184" height="184">
    <circle cx="92" cy="92" r="90" fill="rgba(255,255,255,.35)"/>
    <circle cx="92" cy="92" r="72" fill="#fff"/>
    <polygon points="72,58 72,126 126,92" fill="#1ccb8c"/>
  </svg>
</div>

<h2 class="abs center h2" style="top:3127px;font-size:46px">WHY ENROLL!</h2>
<p class="abs center" style="top:3187px;font-size:15px;font-weight:500">To get full access to all the features, start by creating an account</p>

<div class="abs perk" style="left:96px;top:3258px">
  <svg width="70" height="70" fill="none" stroke="#1ccb8c" stroke-width="4"><rect x="4" y="10" width="62" height="56" rx="4"/><line x1="4" y1="24" x2="66" y2="24"/><line x1="20" y1="3" x2="20" y2="15"/><line x1="50" y1="3" x2="50" y2="15"/><g stroke="#fff" stroke-width="5"><path d="M16 36h4M30 36h4M44 36h4M16 48h4M30 48h4M44 48h4"/></g></svg>
  <div class="perk__title">Drops</div>
  <p class="perk__text">Purchase NFTs that are directly sold<br>by top Creators</p>
</div>
<div class="divider" style="left:424px"></div>
<div class="abs perk" style="left:448px;top:3258px">
  <svg width="70" height="70" fill="none" stroke="#1ccb8c" stroke-width="4"><path d="M6 8h58l4 16H2z"/><path d="M8 24v40h54V24"/><rect x="26" y="40" width="18" height="24" stroke="#fff"/></svg>
  <div class="perk__title">Marketplace</div>
  <p class="perk__text">Bid on and auction off rare digital<br>collectibles</p>
</div>
<div class="divider" style="left:774px"></div>
<div class="abs perk" style="left:800px;top:3258px">
  <svg width="70" height="70"><polygon points="35,3 64,19 64,51 35,67 6,51 6,19" fill="none" stroke="#1ccb8c" stroke-width="4"/><text x="35" y="42" text-anchor="middle" font-family="Montserrat, Arial, sans-serif" font-weight="800" font-size="17" fill="#fff">NFT</text></svg>
  <div class="perk__title">My NFTs</div>
  <p class="perk__text">A digital gallery to showcase your<br>collection</p>
</div>

<div class="rule" style="left:0;width:1200px;top:3548px"></div>

<h2 class="abs center h2" style="top:3655px">NEVER MISS A DROP</h2>
<p class="abs center" style="top:3720px;font-size:15px;font-weight:500">Subscribe for the latest news, drops &amp; collectibles</p>
<form class="abs subscribe">
  <span class="subscribe__field">Email</span>
  <span class="subscribe__send">SEND</span>
</form>
<div class="abs consent"><span class="consent__box"></span>By entering my email and subscribing I confirm and agree to the above.</div>
<p class="abs fine" style="left:290px;width:620px;top:3891px;text-align:center">After reading the Privacy Notice, you may subscribe for our newsletter to get special offers and occasional surveys delivered to your inbox. Unsubscribe at any time by clicking on the link in the email.</p>

<footer>
  <div class="abs brand" style="left:470px;top:4068px">
    <span class="brand__dot" style="width:60px;height:60px"></span>
    <span class="brand__name" style="font-size:27px">Kindle Ledger<br>Technologies</span>
  </div>
  <div class="rule" style="top:4172px"></div>
  <nav class="abs center footnav" style="top:4193px">
    <span>ABOUT US</span><span>NEWSROOM</span><span>PATENTS</span><span>CLIENTS</span><span>FAQ</span><span>CONTACT</span>
  </nav>
  <div class="rule" style="top:4234px"></div>
  <p class="abs center" style="top:4254px;font-size:12.5px;font-weight:500">Copyright 2022.All right reserved</p>
</footer>

</body>
</html>
```